Professional Modern Website Design

We are a premium IT services provider to the financial industry based in London. Our company is called Veltra our current holding page is www.veltra-example.co.uk. We require a new website to match our new corporate identity. This project is for the design phase only. Development will be handled in-house. I have attached examples of wire frames we have developed (although open to suggestions for improvement) Our brand document that should demonstrate current brand, inc how we communicate to potential clients and finally mostly completed web-content.
We are looking for designers that can create something that sets us apart from our competitors.
Target Market(s)
IT Decision makers in Finance companies such as; hedge funds, private investment banks etc
Industry/Entity Type
Financial
Number of Pages Required
5+ page
Requirements
Must have
- hexagon elements in the design, unique design.
Nice to have
- Blog and social media feeds
Should not have
- Should not resemble a downloaded template

```html
<!DOCTYPE html>
<html lang="en">
<head>
<meta charset="utf-8">
<title>Veltra – IT Services</title>
<link rel="stylesheet" href="https://fonts.googleapis.com/css2?family=Roboto:wght@400;500;700&display=swap">
<style>
:root{
  --orange:#f15a22;
  --dark:#1e1e1e;
  --darker:#161616;
  --ink:#222;
  --muted:#555;
  --white:#fff;
  --field:#3a3a3a;
}
*{box-sizing:border-box;margin:0;padding:0}
html,body{width:1200px;height:2571px;overflow:hidden;background:var(--white)}
body{font-family:'Roboto',Arial,sans-serif;color:var(--ink);position:relative}
.abs{position:absolute}

/* header */
.site-header{left:0;top:0;width:1200px;height:86px;background:var(--darker)}
.brand{left:86px;top:22px;display:flex;align-items:center;gap:10px;color:var(--orange);font-weight:700;font-size:24px}
.brand-mark{width:22px;height:22px;background:var(--orange)}
.main-nav{top:34px;left:0;width:1200px;font-size:17px;color:var(--white)}
.main-nav span{position:absolute}
.main-nav .active{color:var(--orange)}

/* hero */
.hero{left:0;top:86px;width:1200px;height:423px;background:linear-gradient(180deg,#3b4350 0%,#252a33 55%,#14161b 100%)}
.hero-card{left:86px;top:200px;width:428px;height:214px;background:rgba(255,255,255,.82);padding:22px 26px}
.hero-card h1{font-size:34px;font-weight:700;color:#1d1d1d;margin-bottom:8px}
.hero-card p{font-size:15.5px;line-height:20px;color:#222}
.hero-dots{left:440px;top:377px;display:flex;gap:6px}
.hero-dots i{width:11px;height:11px;border-radius:50%;background:#bbb;display:block}
.hero-dots i:first-child{background:var(--orange)}

/* pillars */
.pillars{left:89px;top:566px;width:234px;height:531px;border:3px solid var(--orange);padding:16px 12px 10px 14px;overflow:hidden}
.pillars h2{font-size:15px;font-weight:700;color:var(--orange);text-align:center;margin-bottom:8px}
.pillars p{font-size:15px;line-height:22.5px;color:#222;margin-bottom:10px;hyphens:auto;-webkit-hyphens:auto}

/* services */
.service{width:300px;text-align:center}
.service svg.hex{display:block;margin:0 auto}
.service h3{font-size:15.5px;font-weight:700;line-height:20px;margin-top:24px;color:#1d1d1d;height:46px;display:flex;align-items:flex-end;justify-content:center}
.service p{font-size:12.5px;line-height:19px;color:#333;margin:0 auto;width:270px;height:118px}
.more-btn{display:inline-block;width:92px;height:32px;line-height:32px;background:var(--orange);color:var(--white);font-size:16px;font-weight:500}

/* contact */
.contact{left:0;top:1729px;width:1200px;height:337px;background:#2a2a2a}
.contact-photo{left:0;top:1729px;width:620px;height:337px;background:linear-gradient(90deg,#6b5a50 0%,#4a423d 55%,#2a2a2a 100%)}
.contact-title{left:654px;top:1755px;font-size:22px;font-weight:400;color:#777;letter-spacing:.5px}
.field{left:654px;width:457px;border:1px solid #777;background:var(--field);color:#888;font-size:14px;padding:7px 10px}
.send-btn{left:654px;top:1997px;width:97px;height:34px;background:var(--orange);color:var(--white);font-weight:700;font-size:15px;text-align:center;line-height:34px}

/* footer */
.site-footer{left:0;top:2066px;width:1200px;height:211px;background:var(--dark)}
.office{font-size:15.5px;line-height:20px;color:var(--white)}
.office h4{color:var(--orange);font-size:15px;font-weight:700;margin-bottom:12px}
.office .row{display:flex;gap:12px;align-items:flex-start;margin-bottom:12px}
.office svg{flex:none}
.foot-brand{left:958px;top:2118px;display:flex;align-items:center;gap:8px;color:var(--orange);font-size:22px;font-weight:700}
.foot-brand .brand-mark{width:20px;height:20px}
.social{left:937px;top:2213px;display:flex;gap:14px}
.social i{display:block;width:36px;height:36px;border:2px solid #ccc;border-radius:50%}

/* map + legal */
.map{left:0;top:2277px;width:1200px;height:260px;background:linear-gradient(135deg,#e8e4d8 0%,#dcd8cc 50%,#e4e0d4 100%)}
.legal{left:0;top:2537px;width:1200px;height:34px;background:var(--orange);color:var(--white);font-size:12px;text-align:center;line-height:34px}
</style>
</head>
<body>

<header class="site-header abs">
  <div class="brand abs"><span class="brand-mark"></span>Veltra</div>
  <nav class="main-nav abs">
    <span class="active" style="left:633px">About</span>
    <span style="left:728px">Services</span>
    <span style="left:843px">Partners</span>
    <span style="left:955px">Clients</span>
    <span style="left:1056px">Contact</span>
  </nav>
</header>

<section class="hero abs" role="img" aria-label="Dusk photograph of city office towers"></section>
<div class="hero-card abs">
  <h1>Our Services</h1>
  <p>Lorem Ipsum is simply dummy text of the printing and typesetting industry. Lorem Ipsum has been the industry's standard dummy text ever since the 1500s, when an unknown printer took a galley of type and scrambled it to make a type specimen book.</p>
</div>
<div class="hero-dots abs"><i></i><i></i><i></i></div>

<aside class="pillars abs">
  <h2>The Veltra Pillars</h2>
  <p>Lorem Ipsum is simply dummy text of the printing and typesetting industry. Lorem Ipsum has been the industry's standard dummy text ever since the 1500s, when an unknown printer took a galley.</p>
  <p>but also the leap into electronic typesetting, remaining essentially unchanged. It was popularised in the 1960s with sages.</p>
  <p>but also the leap into electronic typesetting, remaining essentially unchanged. It was popularised in the 1960s with sages.</p>
</aside>

<!-- Service: data centre -->
<article class="service abs" style="left:436px;top:571px">
  <svg class="hex" width="229" height="272" viewBox="0 0 229 272">
    <polygon points="114.5,0 229,68 229,204 114.5,272 0,204 0,68" fill="var(--orange)"/>
    <g fill="none" stroke="#fff" stroke-width="4" stroke-linejoin="round" stroke-linecap="round">
      <rect x="64" y="92" width="101" height="68" rx="3"/>
      <path d="M100 160v16M129 160v16M90 178h49"/>
      <path d="M80 142l20-18 15 12 26-26"/><path d="M132 108h10v10"/>
    </g>
    <g fill="#fff"><rect x="80" y="146" width="8" height="8"/><rect x="96" y="140" width="8" height="14"/><rect x="112" y="144" width="8" height="10"/><rect x="128" y="134" width="8" height="20"/><rect x="144" y="126" width="8" height="28"/></g>
  </svg>
  <h3>Data Centre &amp; Infrastructure<br>Solution</h3>
  <p>Lorem Ipsum is simply dummy text of the printing and typesetting industry. Lorem Ipsum has been the industry's standard dummy text ever since the 1500s, when an unknown printer took a galley of type and scrambled it to make a type specimen book.</p>
  <span class="more-btn">More</span>
</article>

<!-- Service: IT support -->
<article class="service abs" style="left:841px;top:571px">
  <svg class="hex" width="229" height="272" viewBox="0 0 229 272">
    <polygon points="114.5,0 229,68 229,204 114.5,272 0,204 0,68" fill="var(--orange)"/>
    <g fill="none" stroke="#fff" stroke-width="4" stroke-linejoin="round">
      <path d="M107 86h15l3 14 10 5 12-8 11 11-8 12 5 10 14 3v15l-14 3-5 10 8 12-11 11-12-8-10 5-3 14h-15l-3-14-10-5-12 8-11-11 8-12-5-10-14-3v-15l14-3 5-10-8-12 11-11 12 8 10-5z"/>
      <circle cx="114.5" cy="136" r="20"/>
    </g>
  </svg>
  <h3>It Support, Managed &amp;<br>perfession service</h3>
  <p>Lorem Ipsum is simply dummy text of the printing and typesetting industry. Lorem Ipsum has been the industry's standard dummy text ever since the 1500s, when an unknown printer took a galley of type and scrambled it to make a type specimen book.</p>
  <span class="more-btn">More</span>
</article>

<!-- Service: voice & data -->
<article class="service abs" style="left:56px;top:1151px">
  <svg class="hex" width="229" height="272" viewBox="0 0 229 272">
    <polygon points="114.5,0 229,68 229,204 114.5,272 0,204 0,68" fill="var(--orange)"/>
    <g fill="none" stroke="#fff" stroke-width="4">
      <path d="M114 136L78 100M114 136L154 104M114 136L84 170M114 136L150 172M114 136L116 88"/>
      <circle cx="114" cy="136" r="14"/><circle cx="74" cy="96" r="8"/><circle cx="158" cy="100" r="8"/>
      <circle cx="80" cy="174" r="8"/><circle cx="154" cy="176" r="8"/><circle cx="116" cy="82" r="6"/>
    </g>
  </svg>
  <h3>Voice &amp; data networks</h3>
  <p>Lorem Ipsum is simply dummy text of the printing and typesetting industry. Lorem Ipsum has been the industry's standard dummy text ever since the 1500s, when an unknown printer took a galley of type and scrambled it to make a type specimen book.</p>
  <span class="more-btn">More</span>
</article>

<!-- Service: hosting -->
<article class="service abs" style="left:436px;top:1151px">
  <svg class="hex" width="229" height="272" viewBox="0 0 229 272">
    <polygon points="114.5,0 229,68 229,204 114.5,272 0,204 0,68" fill="var(--orange)"/>
    <g fill="none" stroke="#fff" stroke-width="4" stroke-linecap="round" stroke-linejoin="round">
      <path d="M92 162H80a22 22 0 0 1-2-44a30 30 0 0 1 58-10a24 24 0 0 1 20 54h-18"/>
      <path d="M114 128v54M100 142l14-14 14 14"/>
    </g>
  </svg>
  <h3>Hosting &amp; Clould</h3>
  <p>Lorem Ipsum is simply dummy text of the printing and typesetting industry. Lorem Ipsum has been the industry's standard dummy text ever since the 1500s, when an unknown printer took a galley of type and scrambled it to make a type specimen book.</p>
  <span class="more-btn">More</span>
</article>

<!-- Service: security -->
<article class="service abs" style="left:841px;top:1151px">
  <svg class="hex" width="229" height="272" viewBox="0 0 229 272">
    <polygon points="114.5,0 229,68 229,204 114.5,272 0,204 0,68" fill="var(--orange)"/>
    <g fill="none" stroke="#fff" stroke-width="4" stroke-linejoin="round">
      <path d="M88 126v-16a26 26 0 0 1 52 0v16"/><path d="M96 126v-16a18 18 0 0 1 36 0v16"/>
      <rect x="78" y="126" width="72" height="60" rx="4"/>
      <circle cx="114" cy="150" r="7"/><path d="M114 157v12"/>
    </g>
  </svg>
  <h3>IT security &amp; IRM</h3>
  <p>Lorem Ipsum is simply dummy text of the printing and typesetting industry. Lorem Ipsum has been the industry's standard dummy text ever since the 1500s, when an unknown printer took a galley of type and scrambled it to make a type specimen book.</p>
  <span class="more-btn">More</span>
</article>

<!-- contact -->
<section class="contact abs"></section>
<div class="contact-photo abs" role="img" aria-label="Photograph of a support agent wearing a headset"></div>
<h2 class="contact-title abs">CONTACT VELTRA</h2>
<div class="field abs" style="top:1794px;height:35px">Name</div>
<div class="field abs" style="top:1846px;height:34px">Email</div>
<div class="field abs" style="top:1897px;height:86px">Message</div>
<div class="send-btn abs">SEND</div>

<!-- footer -->
<footer class="site-footer abs"></footer>
<div class="office abs" style="left:86px;top:2090px;width:380px">
  <h4>LONDON OFFICE</h4>
  <div class="row"><svg width="18" height="22" viewBox="0 0 18 22"><path d="M9 1a7 7 0 0 1 7 7c0 6-7 13-7 13S2 14 2 8a7 7 0 0 1 7-7z" fill="none" stroke="#fff" stroke-width="2"/><circle cx="9" cy="8" r="2.5" fill="#fff"/></svg><span>48 Harrow Lane Mayfair,<br>London W1X 4QT</span></div>
  <div class="row"><svg width="22" height="18" viewBox="0 0 22 18"><rect x="1" y="4" width="20" height="13" rx="2" fill="none" stroke="#fff" stroke-width="2"/><path d="M5 4V1h12v3" fill="none" stroke="#fff" stroke-width="2"/><path d="M6 9h2M10 9h2M14 9h2M6 13h2M10 13h2M14 13h2" stroke="#fff" stroke-width="2"/></svg><span>+44 20 7946 0321</span></div>
  <div class="row"><svg width="20" height="20" viewBox="0 0 20 20"><path d="M4 1l4 4-2 3c1 3 3 5 6 6l3-2 4 4-3 3C8 19 1 12 1 4z" fill="#fff"/></svg><span>info@veltra-example.co.uk</span></div>
</div>
<div class="office abs" style="left:529px;top:2090px;width:360px">
  <h4>ESSEX OFFICE</h4>
  <div class="row"><svg width="18" height="22" viewBox="0 0 18 22"><path d="M9 1a7 7 0 0 1 7 7c0 6-7 13-7 13S2 14 2 8a7 7 0 0 1 7-7z" fill="none" stroke="#fff" stroke-width="2"/><circle cx="9" cy="8" r="2.5" fill="#fff"/></svg><span>7 Abbey Works, Abbey<br>Avenue Southend, ESSEX<br>SS0 9QX</span></div>
  <div class="row"><svg width="22" height="18" viewBox="0 0 22 18"><rect x="1" y="4" width="20" height="13" rx="2" fill="none" stroke="#fff" stroke-width="2"/><path d="M5 4V1h12v3" fill="none" stroke="#fff" stroke-width="2"/><path d="M6 9h2M10 9h2M14 9h2M6 13h2M10 13h2M14 13h2" stroke="#fff" stroke-width="2"/></svg><span>+44 20 7946 0321</span></div>
  <div class="row"><svg width="20" height="20" viewBox="0 0 20 20"><path d="M4 1l4 4-2 3c1 3 3 5 6 6l3-2 4 4-3 3C8 19 1 12 1 4z" fill="#fff"/></svg><span>info@veltra-example.co.uk</span></div>
</div>
<div class="foot-brand abs"><span class="brand-mark"></span>Veltra</div>
<div class="social abs"><i></i><i></i><i></i><i></i></div>

<div class="map abs" role="img" aria-label="Street map showing the office location"></div>
<div class="legal abs">© Veltra Limited - Company Registration No: 8812345, Incorporated in England and Wales</div>

</body>
</html>
```